8x8 Social Media Ad - Summit Harbor Expo

Attention Real Estate Agents
Please join us for our
Quarterly Real Estate Training Expo
The 2nd Saturday of February, May, August and November
Our Next Training Expo is _________________________________
From 9 am to 1 pm
at
Marlowe Suites Fernfield Oak Ridge
4187 Copper Meadow Lane, Fernfield, MD 20994
Scheduled Speakers
9:00 am - Malcolm Prewitt - Orientation
9:30 am - Darnell Ockley - Multiple Income Streams / Pivot Program
10:00 am - Keira Lindqvist - Marketing though Social Media
10:45 am - Owen Trask - Generating Business through Lumo-Net
11:30 am - Ada Nwachime - Real Estate Investing
12:15 pm - Gregory Tamsin - (Main Speaker) Training Topic TBA
For more information call Malcolm Prewitt at (240) 555-0182 or email mprewitt@summitharborhomes.example

```html
<!DOCTYPE html>
<html lang="en">
<head>
<meta charset="utf-8">
<title>Summit Harbor Expo – Quarterly Real Estate Training Expo</title>
<link rel="stylesheet" href="https://fonts.googleapis.com/css2?family=Lato:ital,wght@0,400;0,700;0,900;1,700&display=swap">
<style>
  :root{
    --mat:#84b5bb;
    --navy:#0b1f2b;
    --navy-deep:#061219;
    --cyan:#22c3dc;
    --red:#e3221f;
    --white:#ffffff;
    --photo:#2c3a40;
  }
  *{margin:0;padding:0;box-sizing:border-box}
  html,body{width:1200px;height:1200px;overflow:hidden;background:var(--mat)}
  body{position:relative;font-family:"Lato",sans-serif}
  .ad{position:absolute;left:150px;top:150px;width:900px;height:900px;overflow:hidden}
  .ad-backdrop{position:absolute;inset:0;
    background:linear-gradient(160deg,#123442 0%,var(--navy) 45%,var(--navy-deep) 100%)}
  .abs{position:absolute;left:0;width:900px;text-align:center;white-space:nowrap}
  .brand{position:absolute;left:30px;top:44px;display:flex;align-items:center;gap:10px;
    color:var(--cyan);font-weight:900;font-size:26px;text-transform:uppercase;line-height:1}
  .brand-dot{width:18px;height:18px;background:var(--cyan)}
  .attention{top:62px;left:150px;width:600px;color:var(--red);font-weight:900;font-size:42px;letter-spacing:11px}
  .headline{top:116px;color:var(--cyan);font-weight:900;font-size:54px}
  .invite{top:182px;color:var(--white);font-size:31px}
  .expo-title{top:220px;color:var(--cyan);font-weight:900;font-size:34px}
  .details{position:absolute;left:57px;top:278px;width:781px;height:232px;border:3px solid var(--cyan);
    border-radius:20px;box-shadow:0 0 14px var(--cyan),inset 0 0 12px rgba(34,195,220,.6);
    color:var(--white);font-size:25px;line-height:31px;text-align:center;padding-top:21px}
  .details .blank{display:inline-block;width:338px;border-bottom:2px solid var(--white);height:22px;vertical-align:baseline}
  .speakers-title{top:538px;color:var(--cyan);font-weight:700;font-size:20px;letter-spacing:13px}
  .timeline{position:absolute;left:0;top:580px}
  .speaker{position:absolute;top:612px;width:140px;margin-left:-70px;text-align:center}
  .time{color:var(--cyan);font-weight:900;font-size:14px}
  .portrait{display:block;width:124px;height:124px;margin:10px auto 0;border-radius:50%;
    background:radial-gradient(circle at 50% 40%,#56646a,var(--photo));border:2px solid var(--cyan)}
  .name{margin-top:12px;color:var(--cyan);font-weight:900;font-size:13px;text-transform:uppercase;white-space:nowrap}
  .topic{color:var(--white);font-style:italic;font-weight:700;font-size:13px;line-height:17px}
  .footer{top:859px;color:var(--cyan);font-size:16px}
</style>
</head>
<body>
<main class="ad">
  <div class="ad-backdrop" role="img" aria-label="Dusky photo of city high-rise towers"></div>

  <div class="brand"><span class="brand-dot"></span>Summit Harbor</div>

  <h1 class="abs attention">ATTENTION!</h1>
  <h2 class="abs headline">REAL ESTATE AGENTS</h2>
  <p class="abs invite">PLEASE JOIN US FOR OUR</p>
  <h3 class="abs expo-title">QUARTERLY REAL ESTATE TRAINING EXPO</h3>

  <section class="details">
    <p>The 2nd Saturday of February, May, August and November</p>
    <p>Our Next Training Expo is <span class="blank"></span></p>
    <p>From 9 am to 1 pm</p>
    <p>at</p>
    <p>Marlowe Suites Fernfield Oak Ridge</p>
    <p>4187 Copper Meadow Lane, Fernfield, MD 20994</p>
  </section>

  <h4 class="abs speakers-title">SCHEDULED SPEAKERS</h4>

  <svg class="timeline" width="900" height="20" viewBox="0 0 900 20">
    <line x1="55" y1="9" x2="840" y2="9" stroke="#22c3dc" stroke-width="2"/>
    <g fill="#22c3dc">
      <circle cx="100" cy="9" r="4"/><circle cx="239" cy="9" r="4"/><circle cx="378" cy="9" r="4"/>
      <circle cx="517" cy="9" r="4"/><circle cx="656" cy="9" r="4"/><circle cx="795" cy="9" r="4"/>
    </g>
  </svg>

  <div class="speaker" style="left:100px">
    <div class="time">09:00AM</div>
    <span class="portrait" role="img" aria-label="Portrait photo of Malcolm Prewitt"></span>
    <div class="name">Malcolm Prewitt</div>
    <div class="topic">Orientation</div>
  </div>
  <div class="speaker" style="left:239px">
    <div class="time">09:30AM</div>
    <span class="portrait" role="img" aria-label="Portrait photo of Darnell Ockley"></span>
    <div class="name">Darnell Ockley</div>
    <div class="topic">Multiple Income<br>Streams / Pivot<br>Program</div>
  </div>
  <div class="speaker" style="left:378px">
    <div class="time">10:00AM</div>
    <span class="portrait" role="img" aria-label="Portrait photo of Keira Lindqvist"></span>
    <div class="name">Keira Lindqvist</div>
    <div class="topic">Marketing through<br>Social Media</div>
  </div>
  <div class="speaker" style="left:517px">
    <div class="time">10:45AM</div>
    <span class="portrait" role="img" aria-label="Portrait photo of Owen Trask"></span>
    <div class="name">Owen Trask</div>
    <div class="topic">Generating Business<br>through Lumo-Net</div>
  </div>
  <div class="speaker" style="left:656px">
    <div class="time">11:30AM</div>
    <span class="portrait" role="img" aria-label="Portrait photo of Ada Nwachime"></span>
    <div class="name">Ada Nwachime</div>
    <div class="topic">Real Estate<br>Investing</div>
  </div>
  <div class="speaker" style="left:795px">
    <div class="time">12:15PM</div>
    <span class="portrait" role="img" aria-label="Portrait photo of Gregory Tamsin"></span>
    <div class="name">Gregory Tamsin</div>
    <div class="topic">(Main Speaker)<br>Training Topic TBA</div>
  </div>

  <p class="abs footer">For more information call Malcolm Prewitt at (240) 555-0182 or email mprewitt@summitharborhomes.example</p>
</main>
</body>
</html>
```